Banner poster with different motifs

I'm looking for 5 banners and posters in A1 format in the same design, or the similarity must be recognizable...
Kept quite simple with different titles.

1 ballet
2 Contemporary Dance
3 high heels
4 Salsa & Bachata & Zouk
5 Hip Hop

Modern bright colors
it is for the entrance so that the students see here is a dance school

The text may also be included in the image
The photos are for guidance only; some are our own, some are purchased. However, we are permitted to use them, including our logo, of course.

```html
<!DOCTYPE html>
<html lang="en">
<head>
<meta charset="utf-8">
<title>Dance Classes 2025 – Vivaluz Dance Center Frankfurt</title>
<link href="https://fonts.googleapis.com/css2?family=Questrial&family=Montserrat:wght@600&display=swap" rel="stylesheet">
<style>
  :root{
    --ink:#0d0d0d;
    --sun:#f8bb2b;
    --white:#ffffff;
    --mist:#f1f1f1;
    --orange:#f7931e;
    --flame:#ef5a24;
    --coral:#f26a3c;
    --navy:#14233f;
    --plum:#5a2746;
    --teal:#3d9aa6;
    --sky:#4ab8e8;
    --aqua:#7de3d6;
    --royal:#2a47c4;
    --violet:#8f23d6;
    --dots:#d6d6d6;
  }
  *{margin:0;padding:0;box-sizing:border-box}
  html,body{width:1200px;height:4237px;overflow:hidden;background:var(--white)}
  body{font-family:"Questrial",sans-serif;color:var(--ink)}
  .poster{position:relative;width:1200px;height:847px;overflow:hidden;background:var(--white)}
  .poster:last-child{height:849px}
  .backdrop{position:absolute;inset:0;width:1200px;height:100%}
  .card{position:absolute;left:85px;top:84px;width:1030px;height:678px;background:var(--white)}
  .halo{position:absolute;border-radius:50%;background:var(--sun)}
  .photo{position:absolute;border-radius:40% 40% 20% 20%}
  .headline{position:absolute;left:133px;top:38px;font-size:76px;letter-spacing:-2px;line-height:1;white-space:nowrap}
  .headline span{margin-left:22px}
  .year{position:absolute;left:58px;top:150px;font-size:76px;line-height:1;writing-mode:vertical-rl;letter-spacing:-1px}
  .title{position:absolute;font-size:125px;line-height:105px;letter-spacing:-3px;white-space:nowrap}
  .styles{position:absolute;font-size:21px;line-height:31px;list-style:none;white-space:nowrap}
  .styles li::before{content:"•";margin-right:9px}
  .brand{position:absolute;display:flex;flex-direction:column;align-items:center;width:200px;margin-left:-100px}
  .brand-dot{width:46px;height:46px;border:2px solid var(--ink);border-radius:50%;margin-bottom:6px}
  .brand-name{font-size:22px;letter-spacing:1px}
  .tagline{position:absolute;font-family:"Montserrat",sans-serif;font-weight:600;font-size:15px;letter-spacing:.42em;white-space:nowrap}
</style>
</head>
<body>

<!-- Ballet -->
<section class="poster poster--ballet">
  <svg class="backdrop" viewBox="0 0 1200 847" aria-hidden="true">
    <rect width="1200" height="847" fill="var(--mist)"/>
    <path d="M0 0H260C240 90 150 170 0 185Z" fill="var(--orange)"/>
    <path d="M1200 250C1120 320 1110 470 1200 560Z" fill="var(--sky)"/>
    <path d="M1200 0H1100C1140 60 1170 110 1200 120Z" fill="var(--aqua)"/>
    <path d="M0 560C60 610 110 720 210 770C300 820 420 800 560 847H0Z" fill="var(--sky)"/>
    <path d="M780 847C840 760 1000 740 1120 847Z" fill="var(--orange)"/>
    <rect x="0" y="520" width="190" height="320" rx="30" fill="var(--dots)" role="img" aria-label="halftone dot pattern"/>
    <rect x="990" y="0" width="210" height="160" rx="30" fill="var(--dots)" role="img" aria-label="halftone dot pattern"/>
  </svg>
  <div class="card"></div>
  <div class="halo" style="left:674px;top:197px;width:444px;height:444px"></div>
  <div class="photo" role="img" aria-label="Photo of a ballerina in a white tutu on pointe" style="left:690px;top:40px;width:430px;height:760px;background:linear-gradient(180deg,#f4ece6,#e2d6cd)"></div>
  <h1 class="headline">DANCE<span>CLASSES</span></h1>
  <div class="year">2025</div>
  <h2 class="title" style="left:215px;top:205px;font-size:180px;line-height:180px">BALLET</h2>
  <ul class="styles" style="left:228px;top:380px;line-height:38px">
    <li>Ballet</li><li>Contemporary Dance</li><li>High Heels</li><li>Salsa &amp; Bachata &amp; Zouk</li><li>Hip Hop</li>
  </ul>
  <div class="brand" style="left:482px;top:630px"><div class="brand-dot"></div><div class="brand-name">VIVALUZ</div></div>
  <div class="tagline" style="left:224px;top:735px">VIVALUZ DANCE CENTER FRANKFURT</div>
</section>

<!-- Contemporary -->
<section class="poster poster--contemporary">
  <svg class="backdrop" viewBox="0 0 1200 847" aria-hidden="true">
    <defs>
      <linearGradient id="flameGrad" x1="0" y1="0" x2="1" y2="1"><stop offset="0" stop-color="var(--flame)"/><stop offset=".7" stop-color="var(--coral)"/><stop offset="1" stop-color="var(--plum)"/></linearGradient>
      <linearGradient id="nightGrad" x1="0" y1="0" x2="1" y2="1"><stop offset="0" stop-color="var(--plum)"/><stop offset="1" stop-color="var(--navy)"/></linearGradient>
    </defs>
    <path d="M0 0H505L0 505Z" fill="url(#flameGrad)"/>
    <path d="M0 360L360 0H505L0 505Z" fill="var(--plum)" opacity=".7"/>
    <path d="M1200 470V847H825Z" fill="url(#nightGrad)"/>
    <path d="M1200 620V847H1000Z" fill="var(--navy)"/>
    <rect x="0" y="585" width="190" height="262" rx="30" fill="var(--dots)" role="img" aria-label="halftone dot pattern"/>
    <rect x="985" y="0" width="215" height="150" rx="30" fill="var(--dots)" role="img" aria-label="halftone dot pattern"/>
  </svg>
  <div class="halo" style="left:666px;top:132px;width:460px;height:460px"></div>
  <div class="photo" role="img" aria-label="Photo of a male contemporary dancer in black mid-leap" style="left:735px;top:40px;width:330px;height:740px;background:linear-gradient(180deg,#3a2c28,#111)"></div>
  <h1 class="headline">DANCE<span>CLASSES</span></h1>
  <div class="year">2025</div>
  <h2 class="title" style="left:218px;top:180px">CONTEM<br>PORARY<br>DANCE</h2>
  <ul class="styles" style="left:230px;top:533px">
    <li>Ballet / Contemporary Dance /High Heels</li><li>Salsa &amp; Bachata &amp; Zouk / Hip Hop</li>
  </ul>
  <div class="brand" style="left:462px;top:640px"><div class="brand-dot"></div><div class="brand-name">VIVALUZ</div></div>
  <div class="tagline" style="left:220px;top:748px">VIVALUZ DANCE CENTER FRANKFURT</div>
</section>

<!-- High Heels -->
<section class="poster poster--heels">
  <svg class="backdrop" viewBox="0 0 1200 847" aria-hidden="true">
    <defs>
      <linearGradient id="sunsetGrad" x1="0" y1="0" x2="1" y2="1"><stop offset="0" stop-color="var(--coral)"/><stop offset="1" stop-color="var(--orange)"/></linearGradient>
      <linearGradient id="seaGrad" x1="0" y1="0" x2="1" y2="1"><stop offset="0" stop-color="var(--orange)"/><stop offset=".45" stop-color="var(--teal)"/><stop offset="1" stop-color="var(--royal)"/></linearGradient>
    </defs>
    <path d="M0 0H505L0 460Z" fill="url(#sunsetGrad)"/>
    <path d="M1200 430V847H690Z" fill="url(#seaGrad)"/>
    <rect x="0" y="570" width="190" height="277" rx="30" fill="var(--dots)" role="img" aria-label="halftone dot pattern"/>
    <rect x="985" y="0" width="215" height="175" rx="30" fill="var(--dots)" role="img" aria-label="halftone dot pattern"/>
  </svg>
  <div class="halo" style="left:618px;top:117px;width:490px;height:490px"></div>
  <div class="photo" role="img" aria-label="Photo of a kneeling dancer in a black bodysuit, long gloves and thigh-high boots" style="left:660px;top:140px;width:430px;height:520px;background:linear-gradient(180deg,#4a3a36,#0d0d0d)"></div>
  <h1 class="headline">DANCE<span>CLASSES</span></h1>
  <div class="year">2025</div>
  <h2 class="title" style="left:218px;top:205px;font-size:150px;line-height:132px">HIGH<br>HEELS</h2>
  <ul class="styles" style="left:222px;top:495px">
    <li>Ballet / Contemporary Dance / High Heels</li><li>Salsa &amp; Bachata &amp; Zouk / Hip Hop</li>
  </ul>
  <div class="brand" style="left:454px;top:636px"><div class="brand-dot"></div><div class="brand-name">VIVALUZ</div></div>
  <div class="tagline" style="left:222px;top:744px">VIVALUZ DANCE CENTER FRANKFURT</div>
</section>

<!-- Salsa Bachata Zouk -->
<section class="poster poster--latin">
  <svg class="backdrop" viewBox="0 0 1200 847" aria-hidden="true">
    <defs>
      <linearGradient id="duskGrad" x1="0" y1="0" x2="1" y2="1"><stop offset="0" stop-color="var(--royal)"/><stop offset="1" stop-color="var(--violet)"/></linearGradient>
    </defs>
    <rect width="1200" height="847" fill="url(#duskGrad)"/>
    <rect x="965" y="0" width="235" height="200" rx="30" fill="#6b78d8" opacity=".5" role="img" aria-label="halftone dot pattern"/>
    <rect x="0" y="580" width="260" height="267" rx="30" fill="#6b78d8" opacity=".5" role="img" aria-label="halftone dot pattern"/>
  </svg>
  <div class="card" style="top:86px;height:674px"></div>
  <div class="halo" style="left:131px;top:131px;width:494px;height:494px"></div>
  <div class="photo" role="img" aria-label="Photo of a couple in a close salsa embrace" style="left:197px;top:140px;width:346px;height:620px;border-radius:45% 45% 0 0;background:linear-gradient(180deg,#8a6a5c,#5a1f28)"></div>
  <h1 class="headline">DANCE<span>CLASSES</span></h1>
  <div class="year">2025</div>
  <h2 class="title" style="left:575px;top:175px;font-size:120px;line-height:107px">SALSA<br>BACHATA<br>ZOUK</h2>
  <ul class="styles" style="left:576px;top:510px">
    <li>Ballet / Contemporary Dance / High Heels</li><li>Salsa &amp; Bachata &amp; Zouk / Hip Hop</li>
  </ul>
  <div class="brand" style="left:825px;top:628px"><div class="brand-dot"></div><div class="brand-name">VIVALUZ</div></div>
  <div class="tagline" style="left:584px;top:733px">VIVALUZ DANCE CENTER FRANKFURT</div>
</section>

<!-- Hip Hop -->
<section class="poster poster--hiphop">
  <svg class="backdrop" viewBox="0 0 1200 849" aria-hidden="true">
    <defs>
      <linearGradient id="blazeGrad" x1="0" y1="0" x2="1" y2="1"><stop offset="0" stop-color="var(--flame)"/><stop offset="1" stop-color="var(--orange)"/></linearGradient>
    </defs>
    <path d="M0 0H550L0 430Z" fill="url(#blazeGrad)"/>
    <path d="M1200 370V849H560Z" fill="url(#blazeGrad)"/>
    <path d="M1200 560V849H850Z" fill="var(--orange)"/>
    <rect x="0" y="570" width="230" height="279" rx="30" fill="var(--dots)" role="img" aria-label="halftone dot pattern"/>
    <rect x="985" y="0" width="215" height="200" rx="30" fill="var(--dots)" role="img" aria-label="halftone dot pattern"/>
  </svg>
  <div class="halo" style="left:212px;top:187px;width:496px;height:496px"></div>
  <div class="photo" role="img" aria-label="Photo of a female hip hop dancer arching backwards in mid-air" style="left:156px;top:190px;width:404px;height:470px;background:linear-gradient(135deg,#6b4a3a,#c9c4bf)"></div>
  <h1 class="headline">DANCE<span>CLASSES</span></h1>
  <div class="year">2025</div>
  <h2 class="title" style="left:590px;top:272px;font-size:122px">HIP HOP</h2>
  <ul class="styles" style="left:596px;top:425px">
    <li>Ballet / Contemporary Dance / High Heels</li><li>Salsa &amp; Bachata &amp; Zouk / Hip Hop</li>
  </ul>
  <div class="brand" style="left:1003px;top:628px"><div class="brand-dot"></div><div class="brand-name">VIVALUZ</div></div>
  <div class="tagline" style="left:597px;top:748px">VIVALUZ DANCE CENTER FRANKFURT</div>
</section>

</body>
</html>
```